Tallowmere Fitness Business Card - I want exactly the same font than the font on the logo for my Name if possible and address and ETC. or a similar font that will look really good

I need those business cards ASAP so it would be amazing if you can submit your designs as quickly as possible!

Thanks so much

```html
<!DOCTYPE html>
<html lang="en">
<head>
<meta charset="utf-8">
<title>Tallowmere Fitness – Business Cards</title>
<link href="https://fonts.googleapis.com/css2?family=Michroma&display=swap" rel="stylesheet">
<style>
  :root {
    --backdrop: #b8000b;
    --card: #000000;
    --ink: #ffffff;
    --accent: #b8000b;
  }
  html, body {
    margin: 0;
    padding: 0;
    width: 1200px;
    height: 1200px;
    overflow: hidden;
    background: var(--backdrop);
    font-family: "Michroma", sans-serif;
    color: var(--ink);
  }
  .canvas {
    position: relative;
    width: 1200px;
    height: 1200px;
  }
  .card {
    position: absolute;
    width: 531px;
    height: 294px;
    background: var(--card);
  }
  .card--front { left: 335px; top: 282px; }
  .card--staff-a { left: 43px; top: 624px; }
  .card--staff-b { left: 626px; top: 624px; }

  /* Front lockup */
  .lockup {
    position: absolute;
    left: 0; right: 0;
    top: 118px;
    display: flex;
    align-items: center;
    justify-content: center;
    gap: 14px;
  }
  .lockup__square {
    width: 30px;
    height: 30px;
    background: var(--accent);
  }
  .lockup__rule {
    width: 3px;
    height: 56px;
    background: var(--ink);
  }
  .lockup__name {
    font-size: 21px;
    letter-spacing: 0.5px;
    white-space: nowrap;
  }

  /* Staff card */
  .brand-block {
    position: absolute;
    left: 22px;
    top: 104px;
    width: 235px;
    display: flex;
    align-items: center;
    gap: 12px;
  }
  .brand-block__square {
    width: 26px;
    height: 26px;
    background: var(--accent);
    flex: none;
  }
  .brand-block__name {
    font-size: 19px;
    line-height: 1.35;
    letter-spacing: 0.5px;
  }
  .card__rule {
    position: absolute;
    left: 274px;
    top: 31px;
    width: 3px;
    height: 231px;
    background: var(--ink);
  }
  .card__header {
    position: absolute;
    left: 298px;
    top: 57px;
    font-size: 13px;
    line-height: 1.3;
    letter-spacing: 1px;
  }
  .contact {
    position: absolute;
    left: 298px;
    top: 132px;
    font-size: 7.6px;
    line-height: 10.4px;
    white-space: nowrap;
  }
  .contact p { margin: 0; }
  .contact .gap { margin-top: 10.4px; }
</style>
</head>
<body>
<main class="canvas">

  <section class="card card--front" aria-label="Card front">
    <div class="lockup">
      <span class="lockup__square"></span>
      <span class="lockup__rule"></span>
      <span class="lockup__name">TALLOWMERE FITNESS</span>
    </div>
  </section>

  <section class="card card--staff-a" aria-label="Card back – Marcel Dufresne">
    <div class="brand-block">
      <span class="brand-block__square"></span>
      <span class="brand-block__name">TALLOWMERE<br>FITNESS</span>
    </div>
    <span class="card__rule"></span>
    <div class="card__header">TALLOWMERE<br>FITNESS</div>
    <div class="contact">
      <p>Marcel Dufresne</p>
      <p>Director, Strength &amp; Conditioning Head Coach</p>
      <p class="gap">Mobile: 0400 555 218</p>
      <p>mdufresne@tallowmerefitness.com</p>
      <p>www.tallowmerefitness.com/community</p>
      <p class="gap">Brinsford Central - Australia</p>
      <p>Level 4</p>
      <p>72 Calder Row</p>
      <p>Brinsford VIC 3999</p>
      <p class="gap">ABN: 41208553190</p>
    </div>
  </section>

  <section class="card card--staff-b" aria-label="Card back – Nina Vale">
    <div class="brand-block">
      <span class="brand-block__square"></span>
      <span class="brand-block__name">TALLOWMERE<br>FITNESS</span>
    </div>
    <span class="card__rule"></span>
    <div class="card__header">TALLOWMERE<br>FITNESS</div>
    <div class="contact">
      <p>Nina Vale</p>
      <p>Strength &amp; Conditioning Coach</p>
      <p class="gap">Mobile: 0400 555 764</p>
      <p>nvale@tallowmerefitness.com</p>
      <p>www.tallowmerefitness.com/community</p>
      <p class="gap">Brinsford Central - Australia</p>
      <p>Level 4</p>
      <p>72 Calder Row</p>
      <p>Brinsford VIC 3999</p>
      <p class="gap">ABN: 41208553190</p>
    </div>
  </section>

</main>
</body>
</html>
```